Inspirational Card with Words of Wisdom to Give to Kids

I run basketball camps and give inspirational messages to elementary schools and high schools (www.brightpathcourts.com).

I would like to create a card that has some inspirational thoughts and words of wisdom on it that I can give away...and that students and athletes will keep in their wallet as a reminder of things I've taught them.

I want it to be clean and classy, while not looking too child-like or business-like, as I'd like to be able to give it out to kids, teenagers, and young adults.

The card will be the size of a regular business card and will be double-sided. I would like to use black, orange, gray, and white as the primary colors, with white or gray likely being the background color.
Updates

You're welcome to leave off the title "Lessons to Carry" if desired and just use "The Golden Compass of Growth" on the front of the card.

Thanks.

If you choose to leave off the poem, which you're welcome to do, please make one minor addition to the 5-point creed:

Add the words "God and" to "Honour others in everything you say and do" so it becomes:

"Honour God and others in everything you say and do."

Target Market(s)

Children, Teenagers, and Young Adults

Industry/Entity Type

Business

Requirements
Must have
• All the content, although the poem could be removed if necessary.
Should not have
• Nothing basketball-specific, as I want to be able to give it out to any child or teenager.

```html
<!DOCTYPE html>
<html lang="en">
<head>
<meta charset="utf-8">
<title>The Golden Compass of Growth – Wallet Card</title>
<link rel="stylesheet" href="https://fonts.googleapis.com/css2?family=Cinzel:wght@600&family=Source+Sans+3:ital,wght@0,400;0,600;0,700;1,400;1,700&display=swap">
<style>
  :root {
    --orange: #f06a24;
    --slate: #6b7880;
    --ink: #1d1d1d;
    --text: #333333;
    --paper: #ffffff;
    --backdrop: #e7e3de;
    --sans: "Source Sans 3", "Myriad Pro", Arial, sans-serif;
    --serif: "Cinzel", "Trajan Pro", Georgia, serif;
  }
  * { box-sizing: border-box; margin: 0; padding: 0; }
  html, body { width: 960px; height: 1200px; overflow: hidden; }
  body { background: var(--backdrop); font-family: var(--sans); color: var(--text); position: relative; }

  .card {
    position: absolute; left: 60px; width: 840px; height: 480px;
    background: var(--paper); border-radius: 30px; overflow: hidden;
    box-shadow: 6px 8px 14px rgba(0,0,0,.35);
  }
  .card--front { top: 72px; }
  .card--back { top: 638px; }

  /* Front */
  .front__band { position: absolute; left: 0; top: 0; width: 100%; height: 61px; background: var(--orange); }
  .front__tab {
    position: absolute; left: 280px; top: 0; width: 282px; height: 61px; background: var(--paper);
    display: flex; align-items: flex-end; justify-content: center; padding-bottom: 2px;
    font-weight: 700; font-style: italic; font-size: 29px; color: var(--slate); letter-spacing: .3px; text-transform: uppercase;
  }
  .front__title {
    position: absolute; left: 0; top: 78px; width: 100%; text-align: center;
    font-family: var(--serif); font-weight: 600; font-size: 40px; color: var(--ink); letter-spacing: 1px;
  }
  .rules { position: absolute; left: 0; top: 133px; width: 100%; display: flex; gap: 8px; }
  .rules__col { flex: 1; }
  .rules__col:nth-child(1) { flex: 0 0 276px; }
  .rules__col:nth-child(3) { flex: 0 0 276px; }
  .rules__head {
    height: 37px; background: var(--slate); color: var(--paper); text-align: center;
    font-weight: 700; font-style: italic; font-size: 27px; line-height: 40px; text-transform: uppercase;
  }
  .rules__list {
    list-style: none; background: var(--orange); height: 98px; padding-top: 4px;
    text-align: center; color: var(--ink); font-size: 22px; line-height: 31px;
  }
  .poem__lead {
    position: absolute; left: 0; top: 280px; width: 100%; text-align: center;
    font-weight: 700; font-style: italic; font-size: 24px; color: var(--text);
  }
  .poem__lines {
    position: absolute; left: 35px; top: 322px; width: 790px;
    display: grid; grid-template-columns: 420px 1fr; row-gap: 10px; list-style: none;
    font-size: 19.5px; color: #444;
  }
  .poem__lines li::before { content: "▪"; font-size: 14px; margin-right: 16px; position: relative; top: -2px; }
  .poem__cite {
    position: absolute; left: 0; top: 395px; width: 100%; text-align: center;
    font-style: italic; font-size: 18px; color: #555;
  }
  .front__footer {
    position: absolute; left: 0; bottom: 0; width: 100%; height: 52px; background: var(--orange);
    display: flex; align-items: center; justify-content: center; gap: 6px; color: var(--ink);
  }
  .front__quote { font-weight: 700; font-style: italic; font-size: 26px; }
  .front__author { font-size: 21px; }

  /* Back */
  .back__band {
    position: absolute; left: 0; top: 0; width: 100%; height: 59px; background: var(--orange);
    text-align: center; font-weight: 700; font-style: italic; font-size: 35px; line-height: 66px; color: var(--ink);
  }
  .creed {
    position: absolute; left: 0; top: 66px; width: 100%; list-style: none; text-align: center;
    font-size: 21px; line-height: 39.3px; color: #3a3a3a;
  }
  .creed li::before { content: "▪"; font-size: 13px; margin-right: 5px; position: relative; top: -2px; }
  .pledge__title {
    position: absolute; left: 0; top: 284px; width: 100%; text-align: center;
    font-weight: 700; font-style: italic; font-size: 26px; color: #444;
  }
  .pledge__text {
    position: absolute; left: 0; top: 327px; width: 100%; text-align: center; font-size: 20.5px; color: #3a3a3a;
  }
  .pledge__fields {
    position: absolute; left: 21px; top: 374px; width: 800px; display: flex; align-items: baseline;
    font-weight: 700; font-style: italic; font-size: 27px; color: var(--ink);
  }
  .pledge__line { display: inline-block; border-bottom: 1.5px solid var(--ink); height: 22px; margin: 0 12px 0 12px; }
  .pledge__line--date { width: 314px; }
  .pledge__line--sign { width: 254px; margin-right: 0; }
  .back__footer {
    position: absolute; left: 0; bottom: 0; width: 100%; height: 60px; background: var(--orange);
    text-align: center; font-weight: 700; font-style: italic; font-size: 27px; line-height: 60px; color: var(--ink); word-spacing: 2px;
  }
</style>
</head>
<body>

<section class="card card--front" aria-label="Card front">
  <div class="front__band"></div>
  <div class="front__tab">Lessons to Carry</div>
  <h1 class="front__title">The Golden Compass of Growth</h1>

  <div class="rules">
    <div class="rules__col">
      <div class="rules__head">Never</div>
      <ul class="rules__list"><li>Lie</li><li>Cheat</li><li>Steal</li></ul>
    </div>
    <div class="rules__col">
      <div class="rules__head">Don’t</div>
      <ul class="rules__list"><li>Blame</li><li>Complain</li><li>Give Up</li></ul>
    </div>
    <div class="rules__col">
      <div class="rules__head">Always</div>
      <ul class="rules__list"><li>Be Grateful</li><li>Uplift Others</li><li>Do More Than Your Share</li></ul>
    </div>
  </div>

  <p class="poem__lead">Four things a man must learn to do If he would make his life more true</p>
  <ul class="poem__lines">
    <li>To think without confusion clearly,</li>
    <li>To love his fellow man sincerely,</li>
    <li>To act from honest motives purely,</li>
    <li>To trust in God and Heaven securely.</li>
  </ul>
  <p class="poem__cite">Rev. Elias Marlowe</p>

  <footer class="front__footer">
    <span class="front__quote">Make each day your masterpiece.</span>
    <span class="front__author">- Coach Dale Harmon</span>
  </footer>
</section>

<section class="card card--back" aria-label="Card back">
  <h2 class="back__band">A 5-Point Creed</h2>
  <ul class="creed">
    <li>Be intentional to grow and learn new things each day.</li>
    <li>Honour others in everything you say and do.</li>
    <li>Act with integrity and uprightness in all matters.</li>
    <li>Prioritize serving and giving to others above yourself.</li>
    <li>Dream, pray, and expect for the impossible</li>
  </ul>

  <h3 class="pledge__title">Golden Compass &amp; 5-Point Creed Pledge:</h3>
  <p class="pledge__text">I commit to doing my best to live out the Golden Compass and 5-Point Creed each day.</p>
  <div class="pledge__fields">
    <span>Date</span><span class="pledge__line pledge__line--date"></span>
    <span>Signature</span><span class="pledge__line pledge__line--sign"></span>
  </div>

  <footer class="back__footer">* Passion &nbsp;* Wonder &nbsp;* Playfulness &nbsp;* Gratitude &nbsp;*Love</footer>
</section>

</body>
</html>
```